!st birthday celebration

Im looking for a celebration type of flyer for our first birthday. something colorful and eye catching but with a vintage feel to it. we are a vintage shop with a friendly atmosphere and always have music playing. I have attached a draft copy i have been working on so far. Thanks

Industry/Entity Type

Shop

```html
<!DOCTYPE html>
<html lang="en">
<head>
<meta charset="utf-8">
<title>First Birthday Celebration – Festivities</title>
<link rel="stylesheet" href="https://fonts.googleapis.com/css2?family=Nunito+Sans:wght@400;700&display=swap">
<style>
  :root {
    --ink: #111111;
    --festive-red: #c8102e;
    --paper: #ffffff;
    --gold: #f7d21a;
    --amber: #f4a81c;
    --tangerine: #f57f17;
    --night: #0b0b0b;
  }
  html, body {
    margin: 0;
    padding: 0;
    width: 1200px;
    height: 900px;
    overflow: hidden;
  }
  .flyer {
    position: relative;
    width: 1200px;
    height: 900px;
    overflow: hidden;
    background: linear-gradient(160deg, var(--gold) 0%, var(--amber) 45%, var(--gold) 70%, var(--amber) 100%);
    font-family: "Nunito Sans", "Avenir Next", sans-serif;
  }
  .ornament-panel {
    position: absolute;
    top: 0;
    width: 252px;
    height: 900px;
    background:
      radial-gradient(circle at 50% 46%, var(--gold) 0 28px, transparent 30px),
      radial-gradient(ellipse at 30% 20%, var(--tangerine) 0 60px, transparent 62px),
      radial-gradient(ellipse at 70% 75%, var(--tangerine) 0 70px, transparent 72px),
      linear-gradient(180deg, var(--night) 0%, #2a1604 50%, var(--night) 100%);
  }
  .ornament-panel--left { left: 0; border-right: 14px solid var(--gold); box-sizing: border-box; }
  .ornament-panel--right { right: 0; border-left: 14px solid var(--gold); box-sizing: border-box; }
  .content-card {
    position: absolute;
    left: 291px;
    top: 42px;
    width: 618px;
    height: 814px;
    background: var(--paper);
    text-align: center;
  }
  .festivities-heading {
    position: absolute;
    top: 113px;
    left: 0;
    right: 0;
    margin: 0;
    font-size: 26px;
    font-weight: 400;
    color: var(--ink);
  }
  .festivities-heading span {
    text-decoration: underline;
    text-underline-offset: 6px;
    text-decoration-thickness: 1.5px;
  }
  .festivities-list {
    list-style: none;
    margin: 0;
    padding: 0;
    position: absolute;
    top: 163px;
    left: 0;
    right: 0;
  }
  .festivities-list li {
    height: 66.6px;
    line-height: 36px;
    font-size: 26px;
    color: var(--festive-red);
    letter-spacing: 0.3px;
  }
  .contact-block {
    position: absolute;
    top: 683px;
    left: 0;
    right: 0;
    font-style: normal;
    font-weight: 700;
    font-size: 20px;
    color: var(--ink);
    line-height: 32.5px;
  }
</style>
</head>
<body>
  <main class="flyer">
    <div class="ornament-panel ornament-panel--left" role="img" aria-label="Decorative black, orange and yellow floral scroll pattern"></div>
    <div class="ornament-panel ornament-panel--right" role="img" aria-label="Decorative black, orange and yellow floral scroll pattern"></div>

    <section class="content-card">
      <h2 class="festivities-heading"><span>Festivities will include</span></h2>
      <ul class="festivities-list">
        <li>music</li>
        <li>refreshments</li>
        <li>face painting</li>
        <li>psychic readings</li>
        <li>pop-up market stalls</li>
        <li>vintage cars on display</li>
        <li>best-dressed vintage outfit</li>
      </ul>
      <address class="contact-block">
        <div>1288 Bayview Coast Rd, Redgum</div>
        <div>Ph: 59 812....</div>
        <div>Mobile: 0491570156</div>
      </address>
    </section>
  </main>
</body>
</html>
```